Falcrest security business card

Looking for a business card for my security company

Target Market(s)

Security

Industry/Entity Type

Security

Contact Information for Business Card

Name - Gil Marston. Title - General manager - direct 314 862.4490 website www. falcrestsecurityservices.example email - gil@ falcrestsecurityservices.example

Requirements
Must have
• Logo attached

```html
<!DOCTYPE html>
<html lang="en">
<head>
<meta charset="utf-8">
<title>Falcrest Security Services – Business Cards</title>
<link href="https://fonts.googleapis.com/css2?family=Mulish:wght@400;600&display=swap" rel="stylesheet">
<style>
  :root {
    --backdrop: #c0bbbc;
    --ink: #231f20;
    --paper: #ffffff;
    --night: #231f20;
    --gold: #c6a04f;
    --gold-light: #e9d6a6;
    --cream: #f3e3a6;
  }
  * { margin: 0; padding: 0; box-sizing: border-box; }
  html, body {
    width: 1040px; height: 1200px; overflow: hidden;
    background: var(--backdrop);
    font-family: "Mulish", sans-serif;
  }
  .card {
    position: absolute;
    width: 853px; height: 468px;
    overflow: hidden;
  }
  .card--front { left: 94px; top: 79px; background: var(--paper); color: var(--ink); }
  .card--back { left: 95px; top: 641px; width: 849px; height: 469px; background: var(--night); color: var(--cream); }
  .card__art { position: absolute; inset: 0; }
  .card__pattern {
    position: absolute; inset: 0;
    background: radial-gradient(ellipse at 92% 85%, #6d6a6b 0%, #3a3637 35%, #262223 70%);
  }
  .identity { position: absolute; left: 69px; top: 110px; }
  .identity__name { font-size: 40px; font-weight: 400; line-height: 1; letter-spacing: 0.2px; }
  .identity__title {
    display: inline-block; margin-top: 10px;
    font-size: 21px; line-height: 1.2; padding-bottom: 2px;
    border-bottom: 1.5px solid currentColor;
  }
  .brand {
    position: absolute; top: 112px;
    transform: translateX(-50%);
    font-size: 56px; font-weight: 600; letter-spacing: 1px;
    color: var(--gold); line-height: 1;
  }
  .card--front .brand { left: 638px; }
  .card--back .brand { left: 590px; }
  .contacts { position: absolute; left: 69px; top: 334px; list-style: none; }
  .contacts__item {
    display: flex; align-items: center; height: 32px;
    font-size: 22px;
  }
  .contacts__icon { width: 20px; height: 20px; margin-right: 14px; flex: none; }
  .card--front .contacts__icon { fill: var(--gold); }
  .card--back .contacts__icon { fill: #ffffff; }
</style>
</head>
<body>

<section class="card card--front">
  <svg class="card__art" viewBox="0 0 853 468" width="853" height="468" aria-hidden="true">
    <defs>
      <linearGradient id="goldEdge" x1="0" y1="0" x2="1" y2="1">
        <stop offset="0" stop-color="#c6a04f"/>
        <stop offset="0.35" stop-color="#ffffff"/>
        <stop offset="0.7" stop-color="#c6a04f"/>
        <stop offset="1" stop-color="#e9d6a6"/>
      </linearGradient>
    </defs>
    <polygon points="178,0 218,0 742,468 736,468" fill="url(#goldEdge)"/>
    <polygon points="218,0 853,0 853,468 742,468" fill="#231f20"/>
  </svg>
  <div class="identity">
    <h1 class="identity__name">Gil Marston</h1>
    <p class="identity__title">General manager</p>
  </div>
  <div class="brand">FALCREST</div>
  <ul class="contacts">
    <li class="contacts__item">
      <svg class="contacts__icon" viewBox="0 0 24 24"><path d="M6.6 10.8a15 15 0 0 0 6.6 6.6l2.2-2.2a1 1 0 0 1 1-.25 11.4 11.4 0 0 0 3.6.57 1 1 0 0 1 1 1V20a1 1 0 0 1-1 1A17 17 0 0 1 3 4a1 1 0 0 1 1-1h3.5a1 1 0 0 1 1 1c0 1.25.2 2.45.57 3.57a1 1 0 0 1-.25 1z"/></svg>
      Direct: 314 862.4490
    </li>
    <li class="contacts__item">
      <svg class="contacts__icon" viewBox="0 0 24 24"><path d="M2 5h20v14H2z M3 6l9 7 9-7" stroke="#fff" stroke-width="1.4"/></svg>
      Email:&nbsp; gil@falcrestsecurityservices.example
    </li>
    <li class="contacts__item">
      <svg class="contacts__icon" viewBox="0 0 24 24"><path d="M6 2l13 12h-6l3.5 7-2.5 1-3.5-7L6 19z"/></svg>
      www.falcrestsecurityservices.example
    </li>
  </ul>
</section>

<section class="card card--back">
  <div class="card__pattern" role="img" aria-label="Scattered paw print pattern in shades of grey"></div>
  <div class="identity">
    <h2 class="identity__name">Gil Marston</h2>
    <p class="identity__title">General manager</p>
  </div>
  <div class="brand">FALCREST</div>
  <ul class="contacts">
    <li class="contacts__item">
      <svg class="contacts__icon" viewBox="0 0 24 24"><path d="M6.6 10.8a15 15 0 0 0 6.6 6.6l2.2-2.2a1 1 0 0 1 1-.25 11.4 11.4 0 0 0 3.6.57 1 1 0 0 1 1 1V20a1 1 0 0 1-1 1A17 17 0 0 1 3 4a1 1 0 0 1 1-1h3.5a1 1 0 0 1 1 1c0 1.25.2 2.45.57 3.57a1 1 0 0 1-.25 1z"/></svg>
      Direct: 314 862.4490
    </li>
    <li class="contacts__item">
      <svg class="contacts__icon" viewBox="0 0 24 24"><path d="M2 5h20v14H2z M3 6l9 7 9-7" stroke="#231f20" stroke-width="1.4"/></svg>
      Email:&nbsp; gil@falcrestsecurityservices.example
    </li>
    <li class="contacts__item">
      <svg class="contacts__icon" viewBox="0 0 24 24"><path d="M6 2l13 12h-6l3.5 7-2.5 1-3.5-7L6 19z"/></svg>
      www.falcrestsecurityservices.example
    </li>
  </ul>
</section>

</body>
</html>
```